Photo Storage Service - Web Application

This is web design for a simple photo storage service.
There is a web page and on the left side is a list of folders and on the right side there are photo thumbnails. By pressing a photo thumbnail, they will see the full size (it's just a link to a different page).
This project is limited only to ONE page, which is the page with the folders list and the thumbnails. However it contains some features that I will try to list here:
- Name of the service: Teso Vault
- Location of account: http://username.tesovault.example
- Folder list: Show all folders belonging to the user. Because you have to be able to drag photos to a folder, they have to be visible and cannot be hidden behind a menu item etc.
- Thumbnails with photos (in the future also videos)
- Adjusted view with smaller thumbnails and less space for folder list (so it is possible to view a larger quantity of thumbnails)- Select multiple thumbnails with rectangle- Show that a thumbnail is selected (maybe bold border?)
- Simple mobile view, but no emphasis on the mobile view in this design project.
- Drag one or more selected photos to a folder
- Delete one or more selected photos
- Drag a folder to another folder
- Rename folder
- Delete folder
- Create folder
- Show progress when deleting/moving (because it calls for every photo, so if there are 100 photos, it will delete 1 by 1 and it will take about 10 seconds - you could show progress bar or equivalent)
Background information: This is for a photo storage service NOT intended for sharing photos, but intended to indefinitely store photos and for yourself to browse your own photos.
It is a design requirement that it loads extremely fast. So we need to limit as much as possible extra graphics that cannot be done by CSS and other external libraries.
(I know this is ONLY design and nothing to do with CSS or libraries, but I can assess from the design if it might be heavy to load when implemented)
I have attached a crude screenshot of the current design, just for your understanding. It should not match this design and you are not in any way supposed to FIT your design into this same style or structure.
Target Market(s)
Consumers
Number of Pages Required
1 page

```html
<!DOCTYPE html>
<html lang="en">
<head>
<meta charset="utf-8">
<title>Teso Vault – My Photos</title>
<link rel="stylesheet" href="https://fonts.googleapis.com/css2?family=Poppins:wght@300;400;500;600&display=swap">
<style>
  :root {
    --brand: #47c68b;
    --brand-icon: #4cc48a;
    --brand-deep: #2f7a55;
    --card: #d4d4d4;
    --ink: #2b2b2b;
    --ink-soft: #4a4a4a;
    --white: #ffffff;
    --menu: #e9e9e9;
  }
  * { box-sizing: border-box; margin: 0; padding: 0; }
  html, body { width: 1200px; height: 654px; overflow: hidden; background: var(--white); }
  body { position: relative; font-family: "Poppins", sans-serif; color: var(--ink); }

  .site-header { position: absolute; left: 0; top: 0; width: 1200px; height: 60px; background: var(--brand); }
  .brand { position: absolute; left: 151px; top: 30px; display: flex; align-items: center; gap: 7px; color: var(--white); font-size: 15px; font-weight: 600; }
  .brand-dot { width: 14px; height: 14px; border-radius: 50%; background: var(--white); }
  .main-nav { position: absolute; top: 41px; left: 731px; display: flex; font-size: 10px; color: var(--ink); }
  .main-nav a { position: absolute; white-space: nowrap; color: inherit; text-decoration: none; }
  .main-nav .is-active { color: var(--white); }
  .user-menu { position: absolute; left: 995px; top: 40px; display: flex; align-items: center; gap: 3px; font-size: 10px; color: var(--ink-soft); }
  .user-dropdown { position: absolute; left: 976px; top: 57px; width: 75px; height: 25px; background: var(--menu); font-size: 6px; color: var(--ink-soft); }
  .user-dropdown span { position: absolute; right: 5px; }
  .user-dropdown .item-settings { top: 3px; }
  .user-dropdown .item-logout { top: 15px; }
  .user-dropdown .divider { position: absolute; left: 0; top: 12px; width: 100%; height: 1px; background: var(--brand); }

  .section-title { position: absolute; font-size: 15px; font-weight: 500; color: var(--ink); }
  .folders-title { left: 151px; top: 106px; }
  .images-title { left: 548px; top: 106px; }

  .folder { position: absolute; left: 151px; width: 301px; height: 52px; background: var(--card); border-radius: 6px; display: flex; align-items: center; }
  .folder.is-target { border: 3px solid var(--brand); height: 51px; }
  .folder .handle { position: absolute; left: 15px; top: 50%; transform: translateY(-50%); }
  .folder .name { position: absolute; left: 61px; font-size: 13.5px; color: var(--ink-soft); }
  .folder.is-target .name { left: 58px; }
  .folder .name.is-editing { border-bottom: 1px solid var(--ink-soft); line-height: 1.2; }
  .folder .trash { position: absolute; right: 16px; top: 50%; transform: translateY(-50%); }
  .folder.is-target .trash { right: 13px; }

  .add-button { position: absolute; width: 37px; height: 37px; background: var(--card); border-radius: 5px; display: flex; align-items: center; justify-content: center; }
  .add-folder { left: 151px; top: 419px; }
  .add-image { left: 1011px; top: 511px; }

  .image-toolbar { position: absolute; left: 548px; top: 128px; display: flex; align-items: center; font-size: 10px; color: var(--ink-soft); }
  .checkbox { width: 11px; height: 11px; border: 2px solid var(--brand); border-radius: 3px; background: var(--white); display: inline-block; }
  .select-all { display: flex; align-items: center; gap: 4px; }
  .delete-selected { margin-left: 28px; color: var(--brand); }

  .thumb { position: absolute; width: 163px; height: 167px; border: 1px solid #bdbdbd; }
  .thumb .checkbox { position: absolute; top: 6px; right: 6px; width: 15px; height: 15px; }
  .col-1 { left: 548px; } .col-2 { left: 717px; } .col-3 { left: 886px; }
  .row-1 { top: 149px; } .row-2 { top: 329px; }
  .thumb-night-peaks { background: linear-gradient(180deg, #0f1630 0%, #27365c 40%, #1d2440 65%, #7a2a5c 88%, #a8386d 100%); }
  .thumb-desert-road { background: linear-gradient(180deg, #4a5e80 0%, #8a96ad 30%, #b0644a 55%, #7d4a36 75%, #4b4541 100%); }
  .thumb-misty-valley { background: linear-gradient(160deg, #3e4140 0%, #8f918e 40%, #d8d8d4 60%, #5b605c 85%, #2e3230 100%); }
  .thumb-rainy-street { background: linear-gradient(180deg, #3b3b3b 0%, #5d5d5c 35%, #2b2b2b 70%, #1c1c1c 100%); }
  .thumb-tower { background: linear-gradient(170deg, #0e1b2e 0%, #1f3a5e 45%, #2c4a6d 65%, #121c2a 100%); }
  .thumb-city-night { background: linear-gradient(180deg, #263747 0%, #3e5263 30%, #1e2a35 60%, #5a4430 85%, #2a2620 100%); }

  .site-footer { position: absolute; left: 0; top: 595px; width: 1200px; height: 59px; background: var(--brand); }
  .copyright { position: absolute; left: 151px; top: 18px; font-size: 10px; color: var(--ink-soft); }
  .footer-links { position: absolute; left: 969px; top: 24px; display: flex; gap: 8px; }
  .footer-links .dot { width: 14px; height: 14px; border-radius: 50%; background: var(--white); }
</style>
</head>
<body>
  <header class="site-header">
    <div class="brand"><span class="brand-dot"></span>Teso Vault</div>
    <nav class="main-nav">
      <a style="left:0">About Us</a>
      <a class="is-active" style="left:80px">My Photos</a>
      <a style="left:169px">Contact Us</a>
    </nav>
    <div class="user-menu">
      <svg width="9" height="10" viewBox="0 0 9 10"><circle cx="4.5" cy="2.6" r="2.4" fill="#fff"/><path d="M0 10 C0 6 9 6 9 10 Z" fill="#fff"/></svg>
      <span>User01</span>
      <svg width="8" height="5" viewBox="0 0 8 5" style="margin-left:1px"><path d="M0 0 L8 0 L4 5 Z" fill="#fff"/></svg>
    </div>
  </header>
  <div class="user-dropdown">
    <span class="item-settings">Account Settings</span>
    <div class="divider"></div>
    <span class="item-logout">Log Out</span>
  </div>

  <h2 class="section-title folders-title">Folders</h2>

  <div class="folder" style="top:149px">
    <svg class="handle" width="24" height="11" viewBox="0 0 24 11"><rect y="0" width="24" height="2" fill="var(--brand-icon)"/><rect y="4.5" width="24" height="2" fill="var(--brand-icon)"/><rect y="9" width="24" height="2" fill="var(--brand-icon)"/></svg>
    <span class="name">A day in Oslo</span>
    <svg class="trash" width="18" height="22" viewBox="0 0 18 22"><rect x="6" y="0" width="6" height="2" rx="1" fill="var(--brand-icon)"/><rect x="0" y="2.5" width="18" height="2.5" rx="1" fill="var(--brand-icon)"/><path d="M2 6.5 H16 L15 22 H3 Z" fill="none" stroke="var(--brand-icon)" stroke-width="2"/><path d="M6.5 9 V19 M9 9 V19 M11.5 9 V19" stroke="var(--brand-icon)" stroke-width="1.4"/></svg>
  </div>
  <div class="folder" style="top:216px">
    <svg class="handle" width="24" height="11" viewBox="0 0 24 11"><rect y="0" width="24" height="2" fill="var(--brand-icon)"/><rect y="4.5" width="24" height="2" fill="var(--brand-icon)"/><rect y="9" width="24" height="2" fill="var(--brand-icon)"/></svg>
    <span class="name">A tour of Svenborg</span>
    <svg class="trash" width="18" height="22" viewBox="0 0 18 22"><g transform="rotate(-18 9 4)"><rect x="6" y="0" width="6" height="2" rx="1" fill="var(--brand-icon)"/><rect x="0" y="2.5" width="18" height="2.5" rx="1" fill="var(--brand-icon)"/></g><path d="M2 6.5 H16 L15 22 H3 Z" fill="none" stroke="var(--brand-icon)" stroke-width="2"/><path d="M6.5 9 V19 M9 9 V19 M11.5 9 V19" stroke="var(--brand-icon)" stroke-width="1.4"/></svg>
  </div>
  <div class="folder" style="top:284px">
    <svg class="handle" width="24" height="11" viewBox="0 0 24 11"><rect y="0" width="24" height="2" fill="var(--brand-icon)"/><rect y="4.5" width="24" height="2" fill="var(--brand-icon)"/><rect y="9" width="24" height="2" fill="var(--brand-icon)"/></svg>
    <span class="name is-editing">Days in Denmark</span>
    <svg class="trash" width="18" height="22" viewBox="0 0 18 22"><rect x="6" y="0" width="6" height="2" rx="1" fill="var(--brand-icon)"/><rect x="0" y="2.5" width="18" height="2.5" rx="1" fill="var(--brand-icon)"/><path d="M2 6.5 H16 L15 22 H3 Z" fill="none" stroke="var(--brand-icon)" stroke-width="2"/><path d="M6.5 9 V19 M9 9 V19 M11.5 9 V19" stroke="var(--brand-icon)" stroke-width="1.4"/></svg>
  </div>
  <div class="folder is-target" style="top:352px">
    <svg class="handle" style="left:12px" width="24" height="11" viewBox="0 0 24 11"><rect y="0" width="24" height="2" fill="var(--brand-icon)"/><rect y="4.5" width="24" height="2" fill="var(--brand-icon)"/><rect y="9" width="24" height="2" fill="var(--brand-icon)"/></svg>
    <span class="name">Brazil</span>
    <svg class="trash" width="18" height="22" viewBox="0 0 18 22"><rect x="6" y="0" width="6" height="2" rx="1" fill="var(--brand-icon)"/><rect x="0" y="2.5" width="18" height="2.5" rx="1" fill="var(--brand-icon)"/><path d="M2 6.5 H16 L15 22 H3 Z" fill="none" stroke="var(--brand-icon)" stroke-width="2"/><path d="M6.5 9 V19 M9 9 V19 M11.5 9 V19" stroke="var(--brand-icon)" stroke-width="1.4"/></svg>
  </div>

  <div class="add-button add-folder"><svg width="16" height="16" viewBox="0 0 16 16"><path d="M8 0 V16 M0 8 H16" stroke="var(--brand-deep)" stroke-width="2"/></svg></div>

  <h2 class="section-title images-title">Images</h2>
  <div class="image-toolbar">
    <span class="select-all"><span class="checkbox"></span>Select All</span>
    <span class="delete-selected">Delete</span>
  </div>

  <a class="thumb thumb-night-peaks col-1 row-1" role="img" aria-label="Snowy mountains at night above a pink-lit road"><span class="checkbox"></span></a>
  <a class="thumb thumb-desert-road col-2 row-1" role="img" aria-label="Desert road through red rock formations at dusk"><span class="checkbox"></span></a>
  <a class="thumb thumb-misty-valley col-3 row-1" role="img" aria-label="Misty granite valley with snow-dusted trees"><span class="checkbox"></span></a>
  <a class="thumb thumb-rainy-street col-1 row-2" role="img" aria-label="Rainy city street lined with parked cars"><span class="checkbox"></span></a>
  <a class="thumb thumb-tower col-2 row-2" role="img" aria-label="Glass skyscraper seen from below at night"><span class="checkbox"></span></a>
  <a class="thumb thumb-city-night col-3 row-2" role="img" aria-label="City skyline at dusk with lit windows"><span class="checkbox"></span></a>

  <div class="add-button add-image"><svg width="16" height="16" viewBox="0 0 16 16"><path d="M8 0 V16 M0 8 H16" stroke="var(--brand-deep)" stroke-width="2"/></svg></div>

  <footer class="site-footer">
    <p class="copyright">Copyright © 2018 Teso Vault</p>
    <div class="footer-links">
      <span class="dot"></span>
      <span class="dot"></span>
      <span class="dot"></span>
      <svg width="14" height="14" viewBox="0 0 14 14"><path d="M1 5 C1 1 13 1 13 5 L10 5 L9 3.5 H5 L4 5 Z" fill="#fff"/><rect x="2.5" y="6" width="9" height="7" rx="1.5" fill="#fff"/><circle cx="7" cy="9.5" r="1.8" fill="var(--brand)"/></svg>
    </div>
  </footer>
</body>
</html>
```